Lindenfield Heart

Business cards for cardiology practice. eventually we will add picture (head shot) but for now just go with full color cards. Will need to use same template and design for three other providers with minor change in the designation besides name.
Looking for a design where logo stands out so as the name.
Industry/Entity Type
Business
Contact Information for Business Card
Tomas Verlund, M.D.
Board Certified in Cardiovascular Disease, Interventional Cardiology & Nuclear Cardiology
312 Harrowgate, Suite K
Brenton, TX 77463
Telephone: (832) 555 0172
FAx: (832) 555-0173
Email: tverlund@lindenfieldheart.example
Web: www. lindenfieldheart.example
Look and feel
Each slider illustrates characteristics of the customer's brand and the style your logo design should communicate.

```html
<!DOCTYPE html>
<html lang="en">
<head>
<meta charset="utf-8">
<title>Lindenfield Heart – Business Card</title>
<link rel="stylesheet" href="https://fonts.googleapis.com/css2?family=Roboto+Condensed:wght@400;700&display=swap">
<style>
  :root {
    --brand-red: #c1202e;
    --text-red: #b3212d;
    --ray-black: #121212;
    --bubble: #ffffff;
    --ink: #141414;
    --stage: #e9e6e1;
  }
  * { box-sizing: border-box; margin: 0; padding: 0; }
  html, body { width: 1200px; height: 1000px; overflow: hidden; }
  body {
    background: var(--stage);
    font-family: "Roboto Condensed", "Arial Narrow", sans-serif;
    color: var(--ink);
    position: relative;
  }
  .business-card {
    position: absolute;
    left: 90px; top: 202px;
    width: 1020px; height: 596px;
    overflow: hidden;
    box-shadow: 0 6px 24px rgba(0,0,0,.25);
  }
  .sunburst-field {
    position: absolute; inset: 0;
    background:
      radial-gradient(ellipse at 60% 48%, rgba(193,32,46,.95) 0%, rgba(193,32,46,.6) 38%, rgba(18,18,18,.9) 82%),
      var(--ray-black);
  }
  .bubble {
    position: absolute;
    background: var(--bubble);
    border-radius: 26px;
  }
  .bubble::after {
    content: "";
    position: absolute;
    width: 22px; height: 22px;
    background: var(--bubble);
  }
  .tail-down-left::after { left: 70px; bottom: -16px; clip-path: polygon(0 0, 100% 0, 0 100%); }
  .tail-down-right::after { right: 110px; bottom: -16px; clip-path: polygon(0 0, 100% 0, 100% 100%); }
  .tail-up-left::after { left: 60px; top: -16px; clip-path: polygon(0 0, 100% 100%, 0 100%); }
  .tail-left::after { left: -14px; top: 120px; clip-path: polygon(100% 0, 100% 100%, 0 100%); }

  .phone-bubble {
    left: 56px; top: 63px; width: 273px; height: 208px;
    text-align: center; padding-top: 22px;
  }
  .phone-bubble .label { font-size: 27px; line-height: 1.2; }
  .phone-bubble .number { font-size: 34px; line-height: 1.25; }
  .phone-bubble .number.primary { color: var(--text-red); margin-bottom: 6px; }

  .brand-bubble {
    left: 372px; top: 38px; width: 588px; height: 226px;
    display: flex; flex-direction: column; align-items: flex-end; justify-content: center;
    padding: 0 34px;
  }
  .brand-name {
    display: flex; align-items: center; gap: 16px;
    font-weight: 700; font-size: 50px; letter-spacing: 1px;
    color: var(--brand-red); text-transform: uppercase; line-height: 1;
    white-space: nowrap;
  }
  .brand-name .mark {
    width: 36px; height: 36px; border-radius: 50%; background: var(--brand-red);
  }
  .brand-tagline {
    margin-top: 16px; font-size: 20px; font-weight: 700; color: var(--ink);
  }

  .provider-bubble {
    left: 147px; top: 302px; width: 500px; height: 137px;
    padding: 14px 26px;
  }
  .provider-name { font-size: 34px; font-weight: 400; color: var(--text-red); margin-bottom: 10px; }
  .provider-credentials { font-size: 19px; line-height: 1.45; }

  .address-bubble {
    left: 693px; top: 332px; width: 280px; height: 224px;
    padding: 22px 20px; font-style: normal;
  }
  .address-practice { font-size: 34px; color: var(--text-red); line-height: 1.2; margin-bottom: 4px; white-space: nowrap; }
  .address-lines { font-size: 34px; line-height: 1.22; }

  .online-bubble {
    left: 83px; top: 466px; width: 560px; height: 94px;
    padding: 16px 26px; font-size: 26px; line-height: 1.2;
  }
</style>
</head>
<body>
  <section class="business-card">
    <div class="sunburst-field" role="img" aria-label="Red and black sunburst rays radiating from the centre of the card"></div>

    <div class="bubble phone-bubble tail-down-left">
      <p class="label">Telephone</p>
      <p class="number primary">(832) 555 0172</p>
      <p class="label">FAX</p>
      <p class="number">(832) 555-0173</p>
    </div>

    <div class="bubble brand-bubble tail-down-right">
      <p class="brand-name"><span class="mark"></span>Lindenfield Heart</p>
      <p class="brand-tagline">Cardiovascular Center of Excellence</p>
    </div>

    <div class="bubble provider-bubble tail-down-left">
      <h1 class="provider-name">Dr. Tomas Verlund</h1>
      <p class="provider-credentials">M.D. Board Certified in Cardiovascular Disease,<br>Interventional Cardiology &amp; Nuclear Cardiology</p>
    </div>

    <div class="bubble online-bubble tail-up-left">
      <p>Email: tverlund@lindenfieldheart.example</p>
      <p>Web: www. lindenfieldheart.example</p>
    </div>

    <address class="bubble address-bubble tail-left">
      <p class="address-practice">Lindenfield Heart</p>
      <p class="address-lines">312 Harrowgate,<br>Suite K Brenton,<br>TX 77463</p>
    </address>
  </section>
</body>
</html>
```